Crest of Morning Paddocks Business Cards with logo

Need a creative business card that pops. Colorful but professional. The attached logo should be included. We are a national horse racing partnership so we are in the equine business. Nothing cartoonlike or whimsical.

Target Market(s)

professionals - 40+

Contact Information for Business Card

Maren Dunleavy
Director of Operations
27 Ashbrook Lane
Middletown, MD. 21584

Phone (313) 555-0147

FX: (949) 555-0192

email: maren@cmpaddocks.example
cmpaddocks.example

Requirements
Must have
• All information above should be on the business card including the website address. Professional yet creative
Nice to have
• an attention grabbing design. not boring. exciting.
Should not have
• cartoon like - whimsical.

```html
<!DOCTYPE html>
<html lang="en">
<head>
<meta charset="utf-8">
<title>Crest of Morning Paddocks – Business Cards</title>
<link href="https://fonts.googleapis.com/css2?family=Libre+Baskerville:wght@400&family=Open+Sans:wght@400&display=swap" rel="stylesheet">
<style>
  :root {
    --navy: #2b2a76;
    --gold: #c8952c;
    --ink: #2a2a2a;
    --paper: #ffffff;
    --backdrop: #e4e4e6;
  }
  * { box-sizing: border-box; margin: 0; padding: 0; }
  html, body { width: 1200px; height: 800px; overflow: hidden; }
  body {
    background: var(--backdrop);
    display: flex;
    align-items: center;
    justify-content: center;
    gap: 40px;
    font-family: "Open Sans", Arial, sans-serif;
  }
  .card {
    width: 540px;
    height: 309px;
    background: var(--paper);
    box-shadow: 0 4px 14px rgba(0,0,0,0.12);
    position: relative;
  }
  .brand {
    display: flex;
    flex-direction: column;
    align-items: center;
    gap: 14px;
  }
  .brand-ring {
    width: 64px;
    height: 64px;
    border: 2px solid var(--gold);
    border-radius: 50%;
  }
  .brand-name {
    font-family: "Libre Baskerville", Georgia, serif;
    color: var(--navy);
    text-transform: uppercase;
    letter-spacing: 0.16em;
    text-align: center;
    line-height: 1.5;
  }

  /* front */
  .card-front {
    display: flex;
    flex-direction: column;
    align-items: center;
    justify-content: center;
    gap: 30px;
  }
  .card-front .brand-name { font-size: 17px; }
  .website {
    font-family: "Libre Baskerville", Georgia, serif;
    color: var(--navy);
    font-size: 13px;
    letter-spacing: 0.22em;
    text-transform: uppercase;
  }

  /* back */
  .card-back {
    display: flex;
    align-items: center;
    padding: 0 34px 0 30px;
    gap: 30px;
  }
  .card-back .brand { width: 190px; }
  .card-back .brand-ring { width: 54px; height: 54px; }
  .card-back .brand-name { font-size: 13px; }
  .contact { flex: 1; }
  .person-name {
    font-family: "Libre Baskerville", Georgia, serif;
    color: var(--navy);
    font-size: 22px;
    line-height: 1.1;
  }
  .person-title {
    font-family: "Libre Baskerville", Georgia, serif;
    color: var(--gold);
    font-size: 13px;
    margin-bottom: 12px;
  }
  .contact-list { list-style: none; font-size: 13px; color: var(--ink); }
  .contact-list li { display: flex; align-items: center; gap: 8px; line-height: 1.75; }
  .contact-icon { width: 13px; height: 13px; flex: none; }
  .address { font-size: 13px; color: var(--ink); line-height: 1.6; margin-top: 8px; }
</style>
</head>
<body>

<section class="card card-front" aria-label="Card front">
  <div class="brand">
    <span class="brand-ring"></span>
    <p class="brand-name">Crest of Morning<br>Paddocks</p>
  </div>
  <p class="website">cmpaddocks.example</p>
</section>

<section class="card card-back" aria-label="Card back">
  <div class="brand">
    <span class="brand-ring"></span>
    <p class="brand-name">Crest of Morning<br>Paddocks</p>
  </div>
  <div class="contact">
    <h1 class="person-name">Maren Dunleavy</h1>
    <p class="person-title">Director of Operations</p>
    <ul class="contact-list">
      <li>
        <svg class="contact-icon" viewBox="0 0 16 16" aria-hidden="true"><path fill="var(--gold)" d="M3.6 1.5l2.2 2.7-1.3 1.6c.9 2 2.6 3.7 4.6 4.6l1.6-1.3 2.7 2.2-1.2 2.2C7 13.3 2.7 9 1.4 2.7z"/></svg>
        (313) 555-0147
      </li>
      <li>
        <svg class="contact-icon" viewBox="0 0 16 16" aria-hidden="true"><path fill="var(--gold)" d="M4 1h7l1 2v3H4zM1 7h14v6h-2v-2H3v2H1zM4 12h8v3H4z"/></svg>
        (949) 555-0192
      </li>
      <li>
        <svg class="contact-icon" viewBox="0 0 16 16" aria-hidden="true"><path fill="var(--gold)" d="M1 3h14v10H1z"/><path fill="none" stroke="#fff" stroke-width="1.2" d="M1.5 3.5L8 9l6.5-5.5"/></svg>
        maren@cmpaddocks.example
      </li>
    </ul>
    <p class="address">27 Ashbrook Lane<br>Middletown, MD. 21584</p>
  </div>
</section>

</body>
</html>
```